Larkspur Ridge Management - Business Cards

I need business cards. My current logo was designed by a designer at this site and I very much like and am happy with the results. I would like a business card that is trendy, unique, current yet professional. I deal with high net worth clients daily

Target Market(s)

Out of state investors looking to get into the rental market in Ohio

Industry/Entity Type

Property Management, Consulting

Contact Information for Business Card

Name, Title (Chief Financial Officer) office phone number (555) 817-3094 website address larkridgemgmt.example

Font styles to use
Sans Serif

Colors
0054AA
0677BA
7BADD7
CADEEF
E8F1F8
0094D4
00A9DD
6FCCEA
C7EBF8
E9F6FB
00AB8E
00BBA5
67D7C9
C6EFE9
E9F9F6

```html
<!DOCTYPE html>
<html lang="en">
<head>
<meta charset="utf-8">
<title>Larkspur Ridge Management – Business Cards</title>
<link href="https://fonts.googleapis.com/css2?family=Montserrat:wght@500;800&display=swap" rel="stylesheet">
<style>
  :root {
    --navy: #1b2b5c;
    --red: #c1222e;
    --paper: #ffffff;
    --ink: #1f2f5e;
    --backdrop: #e4e5e8;
  }
  * { margin: 0; padding: 0; box-sizing: border-box; }
  html, body {
    width: 1200px; height: 799px; overflow: hidden;
    background: var(--backdrop);
    font-family: "Montserrat", Arial, sans-serif;
  }
  .sheet {
    position: relative; width: 1200px; height: 799px;
    display: flex; align-items: center; justify-content: center; gap: 40px;
  }
  .card {
    position: relative; width: 540px; height: 309px; overflow: hidden;
    box-shadow: 0 6px 18px rgba(0,0,0,.18);
  }
  .card--front {
    background: var(--navy);
    display: flex; align-items: center; justify-content: center;
  }
  .card--back { background: var(--paper); }

  .brand {
    display: flex; align-items: center; gap: 12px;
  }
  .brand__mark { width: 18px; height: 18px; flex: none; }
  .brand__name {
    font-weight: 800; font-size: 24px; line-height: 1.15;
    text-transform: uppercase; letter-spacing: .5px; width: 200px;
  }
  .card--front .brand__mark { background: var(--red); }
  .card--front .brand__name { color: var(--paper); }
  .card--back .brand {
    position: absolute; left: 330px; top: 92px;
  }
  .card--back .brand__mark { background: var(--red); }
  .card--back .brand__name { color: var(--navy); font-size: 21px; width: 180px; }

  .bands { position: absolute; inset: 0; width: 540px; height: 309px; }

  .holder { position: absolute; left: 46px; top: 118px; }
  .holder__name {
    color: var(--red); font-weight: 800; font-size: 29px; letter-spacing: .3px;
  }
  .holder__title {
    color: var(--ink); font-weight: 500; font-size: 17px; margin-top: 2px;
  }

  .contact {
    position: absolute; left: 46px; top: 226px;
    list-style: none; color: var(--ink); font-weight: 500; font-size: 15px;
  }
  .contact__item { display: flex; align-items: center; gap: 10px; height: 26px; }
  .contact__icon { width: 16px; height: 16px; flex: none; }
</style>
</head>
<body>
<main class="sheet">
  <section class="card card--front" aria-label="Card front">
    <div class="brand">
      <span class="brand__mark"></span>
      <span class="brand__name">Larkspur Ridge Management</span>
    </div>
  </section>

  <section class="card card--back" aria-label="Card back">
    <svg class="bands" viewBox="0 0 540 309" aria-hidden="true">
      <polygon points="0,0 270,0 262,14 0,14" fill="var(--navy)"/>
      <polygon points="274,0 318,0 310,14 266,14" fill="var(--red)"/>
      <polygon points="250,309 540,309 540,292 258,292" fill="var(--navy)"/>
      <polygon points="202,309 246,309 254,292 210,292" fill="var(--red)"/>
    </svg>

    <div class="holder">
      <p class="holder__name">YOURNAME</p>
      <p class="holder__title">Chief Financial Officer</p>
    </div>

    <div class="brand">
      <span class="brand__mark"></span>
      <span class="brand__name">Larkspur Ridge Management</span>
    </div>

    <ul class="contact">
      <li class="contact__item">
        <svg class="contact__icon" viewBox="0 0 24 24" aria-hidden="true">
          <path d="M6.6 10.8a15.1 15.1 0 0 0 6.6 6.6l2.2-2.2a1 1 0 0 1 1-.25 11.4 11.4 0 0 0 3.6.57 1 1 0 0 1 1 1V20a1 1 0 0 1-1 1A17 17 0 0 1 3 4a1 1 0 0 1 1-1h3.5a1 1 0 0 1 1 1c0 1.25.2 2.45.57 3.57a1 1 0 0 1-.25 1z" fill="var(--ink)"/>
        </svg>
        <span>(555) 817-3094</span>
      </li>
      <li class="contact__item">
        <svg class="contact__icon" viewBox="0 0 24 24" aria-hidden="true" fill="none" stroke="var(--ink)" stroke-width="1.8">
          <circle cx="12" cy="12" r="9"/>
          <ellipse cx="12" cy="12" rx="4" ry="9"/>
          <line x1="3" y1="12" x2="21" y2="12"/>
        </svg>
        <span>www.larkridgemgmt.example</span>
      </li>
    </ul>
  </section>
</main>
</body>
</html>
```